Insurance company needs a business card design

We need a business card design for a Massachusetts-based insurance company Veloria Insurance, LLC. We provide auto insurance to Hispanic (Spanish- or Portuguese-speaking) immigrants in the United States. We will give these business cards to auto dealers where such customers typically go to purchase vehicles. We will provide a solution to the dealers to provide easy insurance to the customers buying cars at their dealerships. Veloria is the Spanish word for protection.
Contact Information for Business Card
Name, Designation, Company Name, Address, Phone Number, Email, Website
Look and feel
Each slider illustrates characteristics of the customer's brand and the style your logo design should communicate.

```html
<!DOCTYPE html>
<html lang="en">
<head>
<meta charset="utf-8">
<title>Veloria Insurance — Business Card</title>
<link rel="stylesheet" href="https://fonts.googleapis.com/css2?family=Montserrat:wght@400;600;700&family=Open+Sans:wght@400&display=swap">
<style>
  :root {
    --navy: #0f4577;
    --navy-deep: #0a3563;
    --blue: #1d5a93;
    --orange: #ef8316;
    --silver: #d9dde2;
    --paper: #ffffff;
    --ink: #3a3a3a;
    --ghost: #e4e4e4;
    --backdrop: #b9b9b9;
  }
  * { box-sizing: border-box; margin: 0; padding: 0; }
  html, body { width: 1200px; height: 876px; overflow: hidden; }
  body {
    background: radial-gradient(ellipse at 40% 30%, #c8c8c8 0%, var(--backdrop) 55%, #a4a4a4 100%);
    display: flex; align-items: center; justify-content: center; gap: 40px;
    font-family: "Montserrat", sans-serif;
  }
  .card {
    position: relative; width: 540px; height: 310px; overflow: hidden;
    box-shadow: 0 10px 24px rgba(0,0,0,.28);
  }
  .card-band {
    position: absolute; left: 0; right: 0; bottom: 0; height: 52px;
    border-top: 4px solid var(--silver);
    display: flex; align-items: center; justify-content: center;
    font-family: "Open Sans", sans-serif; font-size: 12px; letter-spacing: 5px; color: #fff;
  }
  .wordmark { display: flex; align-items: center; gap: 10px; }
  .wordmark-square { width: 22px; height: 22px; }
  .wordmark-name { font-weight: 700; letter-spacing: 1px; text-transform: uppercase; }

  /* front */
  .card-front { background: var(--paper); }
  .card-front .card-band { background: linear-gradient(90deg, var(--navy-deep), var(--blue)); }
  .vehicle-art {
    position: absolute; left: 0; top: 0; width: 230px; height: 254px;
    background: radial-gradient(ellipse at 45% 45%, var(--ghost) 0%, #f1f1f1 55%, var(--paper) 100%);
  }
  .front-body { position: absolute; left: 215px; top: 40px; right: 20px; }
  .front-body .wordmark-square { background: var(--orange); }
  .front-body .wordmark-name { color: var(--navy); font-size: 26px; }
  .holder-name { margin-top: 18px; font-size: 36px; font-weight: 600; line-height: 1; }
  .holder-first { color: var(--navy); font-weight: 400; }
  .holder-last { color: var(--orange); font-weight: 700; }
  .contact-list { list-style: none; margin-top: 16px; font-family: "Open Sans", sans-serif; font-size: 12px; color: var(--ink); }
  .contact-list li { display: flex; align-items: center; gap: 8px; margin-bottom: 4px; }
  .contact-list svg { width: 12px; height: 12px; fill: var(--orange); flex: none; }

  /* back */
  .card-back { background: linear-gradient(135deg, #0d3f74 0%, var(--navy) 45%, #2a5e8c 100%); }
  .card-back .card-band { background: var(--orange); }
  .back-art {
    position: absolute; right: 30px; top: 60px; width: 220px; height: 180px;
    background: radial-gradient(ellipse at center, rgba(30,90,160,.55) 0%, rgba(15,69,119,0) 70%);
  }
  .back-body { position: absolute; inset: 0 0 52px 0; display: flex; align-items: center; justify-content: center; }
  .back-body .wordmark-square { background: #fff; width: 28px; height: 28px; }
  .back-body .wordmark-name { color: #fff; font-size: 34px; }
</style>
</head>
<body>
  <section class="card card-front">
    <div class="vehicle-art" role="img" aria-label="Faint grey line illustration of a car"></div>
    <div class="front-body">
      <div class="wordmark">
        <span class="wordmark-square"></span>
        <span class="wordmark-name">Veloria Insurance</span>
      </div>
      <p class="holder-name"><span class="holder-first">LOREM</span> <span class="holder-last">IPSUM</span></p>
      <ul class="contact-list">
        <li><svg viewBox="0 0 24 24"><path d="M6.6 10.8a15 15 0 0 0 6.6 6.6l2.2-2.2a1 1 0 0 1 1-.25 11.4 11.4 0 0 0 3.6.57 1 1 0 0 1 1 1V20a1 1 0 0 1-1 1A17 17 0 0 1 3 4a1 1 0 0 1 1-1h3.5a1 1 0 0 1 1 1c0 1.25.2 2.45.57 3.6a1 1 0 0 1-.25 1z"/></svg>123 1234 123</li>
        <li><svg viewBox="0 0 24 24"><path d="M2 5h20v14H2zm2 2v.5l8 5 8-5V7z"/></svg>mycompanyid@id.com</li>
        <li><svg viewBox="0 0 24 24"><path d="M12 2a7 7 0 0 0-7 7c0 5.2 7 13 7 13s7-7.8 7-13a7 7 0 0 0-7-7zm0 9.5A2.5 2.5 0 1 1 12 6.5a2.5 2.5 0 0 1 0 5z"/></svg>0/00 lorem ipsum, loremipsum<br>loremipsum-0000</li>
      </ul>
    </div>
    <div class="card-band">www.yourwebsite.com</div>
  </section>

  <section class="card card-back">
    <div class="back-art" role="img" aria-label="Faint blue car illustration"></div>
    <div class="back-body">
      <div class="wordmark">
        <span class="wordmark-square"></span>
        <span class="wordmark-name">Veloria Insurance</span>
      </div>
    </div>
    <div class="card-band">www.yourwebsite.com</div>
  </section>
</body>
</html>
```